Wordpress coded website (5 page-home page, contact form & 3 common pages) for Skiing event

I would like a WordPress site designed for our Ski & Snowboard event. The site is to have 5 total pages.

Hosting has been setup (Bright Hostwell) and WordPress installed.

Requirements:
Front page with Landscape slide, Snowline Social feed, 4 menu items, footer and small description section.

3 Separate pages to be created, with a similar layout with landscape image slider and large text section (content provided)

1 Contact us page with the below form sections
- Name
- School
- Position
- Email
- Phone
- Message

Target Market(s)

School teachers and school students

Industry/Entity Type

Tourism

Number of Pages Required

5+ page

Colors

Designer to choose colors to be used in the design.

Requirements
Must have
• Must include event logo attached in brief. Must include Snowline Social feed on homepage

```html
<!DOCTYPE html>
<html lang="en">
<head>
<meta charset="utf-8">
<title>Kestrel Ski Challenge</title>
<link rel="stylesheet" href="https://fonts.googleapis.com/css2?family=Lilita+One&family=Open+Sans:wdth,wght@75..100,300..700&display=swap">
<style>
  :root {
    --ink: #2f2f2f;
    --muted: #5a5a5a;
    --accent: #1ea5e9;
    --panel: #eeeeee;
    --social: #355591;
    --footer-bar: #d9d9d9;
    --white: #ffffff;
    --divider: #8a8a8a;
    --snow-light: #eeeeef;
    --snow-mid: #dedfe1;
    --snow-dark: #cfd1d4;
  }
  * { margin: 0; padding: 0; box-sizing: border-box; }
  html, body { width: 1200px; height: 960px; overflow: hidden; background: var(--white); }
  body { position: relative; font-family: "Open Sans", Arial, sans-serif; color: var(--ink); }

  .hero {
    position: absolute; left: 0; top: 0; width: 1200px; height: 593px;
    background: linear-gradient(160deg, var(--snow-light) 0%, var(--snow-mid) 55%, var(--snow-dark) 100%);
  }

  .site-header {
    position: absolute; left: 0; top: 0; width: 1200px; height: 95px;
    background: rgba(238,238,238,0.85);
  }
  .brand {
    position: absolute; left: 214px; top: 30px;
    display: flex; align-items: center; gap: 8px;
    font-size: 17px; font-weight: 700; color: var(--accent);
    font-stretch: 80%;
  }
  .brand-dot { width: 22px; height: 22px; border-radius: 50%; background: var(--accent); }
  .main-nav { position: absolute; top: 36px; left: 604px; display: flex; }
  .main-nav a {
    font-size: 19px; color: #222; text-decoration: none; font-stretch: 90%;
    margin-right: 46px;
  }
  .main-nav a:last-child { margin-right: 0; }

  .about {
    position: absolute; left: 214px; top: 417px; width: 770px; height: 225px;
    background: var(--panel); text-align: center;
  }
  .about h1 {
    font-family: "Lilita One", "Arial Black", sans-serif; font-weight: 400;
    color: var(--accent); font-size: 35px; letter-spacing: 0.5px;
    margin-top: 32px; line-height: 1;
  }
  .about p {
    width: 710px; margin: 22px auto 0; font-size: 13px; line-height: 22.5px;
    color: #3c3c3c; font-stretch: 95%;
  }

  .social-feed {
    position: absolute; left: 214px; top: 642px; width: 770px; height: 128px;
    background: var(--social); display: flex; align-items: center; justify-content: center;
    color: var(--white); font-size: 40px; font-weight: 700; letter-spacing: -0.5px;
    font-stretch: 80%;
  }

  .contact-item { position: absolute; text-align: center; color: var(--muted); }
  .contact-item svg { display: block; margin: 0 auto; }
  .address { left: 193px; width: 180px; top: 807px; }
  .address .lines { margin-top: 22px; font-size: 16px; line-height: 19px; font-style: italic; font-stretch: 80%; }
  .phone { left: 470px; width: 222px; top: 808px; }
  .phone .lines { margin-top: 26px; font-size: 21px; font-stretch: 85%; }
  .email { left: 776px; width: 220px; top: 815px; }
  .email .lines { margin-top: 27px; font-size: 13px; color: #444; font-stretch: 95%; white-space: nowrap; }

  .divider {
    position: absolute; top: 799px; height: 125px; width: 0;
    border-left: 2px dotted var(--divider);
  }
  .divider.one { left: 440px; }
  .divider.two { left: 727px; }

  .skier-art {
    position: absolute; left: 958px; top: 840px; width: 232px; height: 94px;
    background: radial-gradient(ellipse 90px 45px at 120px 55px, rgba(190,190,195,0.45), rgba(190,190,195,0) 100%);
  }

  .site-footer {
    position: absolute; left: 0; top: 934px; width: 1200px; height: 26px;
    background: var(--footer-bar); text-align: center;
    font-size: 11.5px; line-height: 26px; color: #555; font-stretch: 85%;
  }
</style>
</head>
<body>
  <div class="hero" role="img" aria-label="Landscape photo slide of a young skier on a snowy slope"></div>

  <header class="site-header">
    <div class="brand"><span class="brand-dot"></span>Kestrel Ski Challenge</div>
    <nav class="main-nav">
      <a href="#">Event</a>
      <a href="#">Mt Kestrel</a>
      <a href="#">Itinerary</a>
      <a href="#">Contact Us</a>
    </nav>
  </header>

  <section class="about">
    <h1>About Us</h1>
    <p>The Kestrel Ski Challenge is the first event of its kind in the Southern Hemisphere offering high school students from Australia to face off against New Zealand locals on the ski fields of Mt Kestrel. With no race experience necessary, the event provides a great fun experience for those enjoying their first time on the slopes as well as providing a chance for experienced skiers and snowboarders to test themselves against the clock and other competitors.</p>
  </section>

  <section class="social-feed">Snowline Social</section>

  <div class="contact-item address">
    <svg width="20" height="26" viewBox="0 0 20 26"><path d="M10 1C5 1 1.5 4.8 1.5 9.5 1.5 15.5 10 25 10 25s8.5-9.5 8.5-15.5C18.5 4.8 15 1 10 1z" fill="var(--accent)"/><circle cx="10" cy="9.5" r="3.6" fill="#fff"/></svg>
    <div class="lines">27 Alpine Ridge Rd.<br>Frostvale, NZ 7791</div>
  </div>

  <div class="divider one"></div>

  <div class="contact-item phone">
    <svg width="24" height="24" viewBox="0 0 24 24"><path d="M6.6 10.8c1.4 2.8 3.8 5.1 6.6 6.6l2.2-2.2c.3-.3.7-.4 1-.2 1.1.4 2.3.6 3.6.6.6 0 1 .4 1 1V20c0 .6-.4 1-1 1C10.6 21 3 13.4 3 4c0-.6.4-1 1-1h3.5c.6 0 1 .4 1 1 0 1.3.2 2.5.6 3.6.1.3 0 .7-.2 1L6.6 10.8z" fill="var(--accent)"/></svg>
    <div class="lines">03 5180 2264</div>
  </div>

  <div class="divider two"></div>

  <div class="contact-item email">
    <svg width="24" height="16" viewBox="0 0 24 16"><rect x="0.5" y="0.5" width="23" height="15" fill="var(--accent)"/><path d="M1 1l11 8 11-8M1 15l8-7M23 15l-8-7" stroke="#fff" stroke-width="1.3" fill="none"/></svg>
    <div class="lines">hello@kestrelskichallenge.example</div>
  </div>

  <div class="skier-art" role="img" aria-label="Faint grey silhouette of a downhill skier"></div>

  <footer class="site-footer">© 2017 All Rights Reserved</footer>
</body>
</html>
```